Commercial construction contractor website.

We need a website that contains About Us, Contact info, Services, Project pictures and Industry News section

Target Market(s)

I'm building industral/flex spaces/commercial.

Industry/Entity Type

Commercial/industrial construction

Coding

Coded - Design and coding required

Number of Pages Required

5+ page

Font styles to use
Other font styles liked:
• The logo font is Microgramma Pro

Requirements
Must have
• Must have correct company name spelling: Halvern Ridge Construction
Nice to have
• I do like to see our logo design implemented in the design
Should not have
• Please do not show big city pictures and business suit people. We are a commercial construction company

```html
<!DOCTYPE html>
<html lang="en">
<head>
<meta charset="utf-8">
<title>Halvern Ridge Construction — Commercial Construction Contractor</title>
<link rel="stylesheet" href="https://fonts.googleapis.com/css2?family=Michroma&family=Montserrat:ital,wght@0,400;0,500;0,600;0,700;1,400&display=swap">
<style>
:root{
  --blue:#0a6fc0;
  --blue-deep:#002a78;
  --blue-mid:#0b5fb0;
  --ink:#2b2b2b;
  --text:#555;
  --muted:#8a8a8a;
  --pale:#f1f3f6;
  --line:#d5d8dc;
  --footer:#111214;
  --white:#fff;
}
*{box-sizing:border-box;margin:0;padding:0}
html,body{width:1200px;height:4717px;overflow:hidden}
body{font-family:"Montserrat",sans-serif;color:var(--text);background:var(--white);position:relative}
.abs{position:absolute}
.display{font-family:"Michroma",sans-serif;color:var(--ink);letter-spacing:-.5px;text-transform:uppercase}
.link{font-weight:600;color:var(--blue);font-size:17px;text-decoration:none;letter-spacing:.3px}
.btn-outline{border:2px solid #9aa3ab;color:var(--blue);font-weight:600;font-size:17px;display:flex;align-items:center;justify-content:center;background:var(--white)}

/* header */
.site-header{top:0;left:0;width:1200px;height:134px;background:var(--white)}
.brand{left:112px;top:40px;display:flex;align-items:center;gap:12px}
.brand-mark{width:34px;height:34px;background:var(--blue)}
.brand-name{font-family:"Montserrat",sans-serif;font-weight:700;font-size:17px;color:var(--blue-mid);line-height:1.2;width:170px}
.top-contact{right:112px;top:28px;font-size:16px;color:var(--text);display:flex;gap:10px;align-items:center}
.top-contact svg{width:13px;height:13px;fill:var(--blue);vertical-align:-1px;margin-right:4px}
.main-nav{right:112px;top:84px;display:flex;gap:28px;font-size:17px;font-weight:500;color:var(--ink)}

/* hero */
.hero{top:134px;left:0;width:1200px;height:588px;background:linear-gradient(180deg,#5f7a9c 0%,#8fa5bd 40%,#9d8f80 70%,#5e4a3a 100%)}
.hero-title{left:112px;top:130px;font-size:48px;line-height:66px;color:var(--white)}
.hero-btn{left:112px;top:353px;width:218px;height:63px;background:var(--white);color:var(--ink);font-weight:600;font-size:19px;display:flex;align-items:center;justify-content:center}
.hero-arrow{top:270px;width:40px;height:46px;background:rgba(20,20,20,.75);display:flex;align-items:center;justify-content:center}
.hero-arrow svg{width:14px;height:14px;stroke:var(--white);stroke-width:2.5;fill:none}

/* welcome */
.welcome-title{left:112px;top:795px;font-size:33px;line-height:43px}
.welcome-copy{left:112px;top:948px;width:490px;font-size:15.5px;line-height:28.5px;color:var(--muted)}
.welcome-btn{left:112px;top:1152px;width:147px;height:55px}
.values{left:632px;top:788px;width:498px;height:421px;background:radial-gradient(circle at 50% 50%,#e6eef8 0%,#ffffff 70%)}
.value{position:absolute;font-size:20px;font-weight:500;color:var(--ink);text-align:center;width:120px}
.value svg{width:28px;height:28px;fill:#4a4f55;display:block;margin:0 auto 10px}

/* services */
.services{top:1295px;left:0;width:1200px;height:660px;background:var(--pale)}
.section-title{left:0;width:1200px;text-align:center;font-size:30px}
.service{width:240px;text-align:center}
.service-icon{width:200px;height:211px;margin:0 auto;background:linear-gradient(135deg,#dfe3e7,#c9d0d6);border-radius:6px}
.service h3{font-weight:500;font-size:23px;line-height:31px;color:var(--ink);margin-top:55px}
.service p{font-size:15px;line-height:26px;color:var(--muted);margin-top:11px}
.service .link{display:block;margin-top:17px}

/* projects */
.project{width:480px;height:342px}
.p1{left:112px;top:2109px;background:linear-gradient(160deg,#3d86d6,#b9c7d4 55%,#7d8a96)}
.p2{left:608px;top:2109px;background:linear-gradient(180deg,#1f5fae 0%,#5a9ad8 45%,#1d4fa0 65%,#4a4d52 100%)}
.p3{left:112px;top:2470px;background:linear-gradient(160deg,#5b4030,#a46a4c 50%,#6e7d48)}
.p4{left:608px;top:2470px;background:linear-gradient(180deg,#b4c2cc 0%,#8fa4b0 45%,#2f5c57 75%,#777 100%)}
.view-more{left:526px;top:2869px;width:148px;height:55px}

/* testimonials */
.testimonials{top:3010px;left:0;width:1200px;height:544px;background:linear-gradient(110deg,#0c7bc4 0%,#0b52a2 50%,#002a78 100%)}
.testimonials .section-title{color:var(--white);top:82px}
.avatar{left:192px;top:214px;width:202px;height:202px;border-radius:50%;background:#e3e5e8}
.quote{left:531px;top:190px;width:515px;font-style:italic;font-size:17.5px;line-height:31.5px;color:#e8f0fa}
.quote-author{left:531px;top:408px;font-size:21px;font-weight:600;color:var(--white)}
.quote-nav{left:987px;top:410px;display:flex;gap:4px}
.quote-nav span{width:19px;height:19px;border-radius:50%;background:#c7d3e2;display:flex;align-items:center;justify-content:center}
.quote-nav svg{width:9px;height:9px;stroke:var(--blue-deep);stroke-width:3;fill:none}

/* news */
.news-card{top:3712px;width:315px;height:509px}
.news-photo{width:315px;height:253px}
.n1{background:linear-gradient(150deg,#8c8f93,#d8a12a 55%,#3c5a8a)}
.n2{background:linear-gradient(180deg,#a9c7e6 0%,#e0c79a 45%,#6b4a33 100%)}
.n3{background:linear-gradient(150deg,#c9ced3,#3a7ecf 45%,#c5d34b 80%)}
.news-body{position:absolute;left:13px;right:13px;top:253px;bottom:0;background:var(--white);box-shadow:0 2px 8px rgba(0,0,0,.12);padding:17px 18px 0 18px}
.news-body h3{font-weight:500;font-size:19px;line-height:28px;color:var(--ink)}
.news-meta{font-size:14.5px;color:var(--muted);margin-top:8px;display:flex;align-items:center;gap:5px}
.news-meta svg{width:13px;height:13px;fill:var(--blue)}
.news-body p{font-size:15px;line-height:26px;color:var(--muted);margin-top:16px}
.news-body .link{display:block;margin-top:14px}

/* footer */
.site-footer{top:4305px;left:0;width:1200px;height:412px;background:var(--footer);color:#d9d9d9}
.footer-divider{top:0;width:1px;height:318px;background:#26282b}
.footer-brand{left:130px;top:208px;width:316px;text-align:center;font-weight:700;font-size:24px;color:#c9ccd1;line-height:1.25}
.footer-col h4{font-weight:600;font-size:19px;color:var(--white);margin-bottom:16px}
.footer-col li{list-style:none;font-size:16px;line-height:33px}
.footer-contact{font-size:16px;line-height:29px}
.footer-contact svg{width:12px;height:13px;fill:var(--blue);margin-right:8px;vertical-align:-1px}
.footer-rule{left:112px;top:319px;width:976px;height:1px;background:#303236}
.copyright{left:112px;top:350px;font-size:16px}
.social{top:338px;width:44px;height:44px;border:2px solid #d9d9d9;border-radius:50%}
</style>
</head>
<body>

<header class="site-header abs">
  <div class="brand abs"><span class="brand-mark"></span><span class="brand-name">Halvern Ridge Construction</span></div>
  <div class="top-contact abs">
    <span><svg viewBox="0 0 24 24"><path d="M6.6 10.8a15.1 15.1 0 0 0 6.6 6.6l2.2-2.2a1 1 0 0 1 1-.25 11.4 11.4 0 0 0 3.6.57 1 1 0 0 1 1 1V20a1 1 0 0 1-1 1A17 17 0 0 1 3 4a1 1 0 0 1 1-1h3.5a1 1 0 0 1 1 1c0 1.25.2 2.45.57 3.57a1 1 0 0 1-.25 1z"/></svg>1 800 555 0142</span>
    <span>|</span>
    <span><svg viewBox="0 0 24 24"><path d="M2 5h20v14H2zm2 2v.5l8 5 8-5V7l-8 5z"/></svg>info@halvernridgeconstruction.com</span>
  </div>
  <nav class="main-nav abs"><span>ABOUT US</span><span>SERVICES</span><span>PROJECT</span><span>NEWS</span><span>CONTACT</span></nav>
</header>

<section class="hero abs" role="img" aria-label="Photo of a multi-storey commercial building under construction with a tower crane">
  <h1 class="hero-title display abs">Commercial<br>Construction<br>Contractor</h1>
  <div class="hero-btn abs">GET MORE INFO</div>
  <div class="hero-arrow abs" style="left:0"><svg viewBox="0 0 14 14"><path d="M9 2 4 7l5 5"/></svg></div>
  <div class="hero-arrow abs" style="right:0"><svg viewBox="0 0 14 14"><path d="M5 2l5 5-5 5"/></svg></div>
</section>

<h2 class="welcome-title display abs">Welcome to<br>Halvern Ridge<br>Construction</h2>
<p class="welcome-copy abs">Lorem ipsum dolor sit amet, consectetur adipiscing elit, sed do eiusmod tempor incididunt ut labore et dolore magna aliqua. Ut enim ad minim veniam, quis nostrud exercitation ullamco laboris nisi ut aliquip ex ea commodo consequatu is aute irure dolor in reprehenderit in voluptate velit esse cill um dolore eu fugiat nulla pariatur oxc.</p>
<div class="welcome-btn btn-outline abs">READ MORE</div>
<div class="values abs" role="img" aria-label="Company values graphic: safety, teamwork and trust">
  <div class="value" style="left:152px;top:72px"><svg viewBox="0 0 24 24"><path d="M12 2 4 5v6c0 5 3.4 9.4 8 11 4.6-1.6 8-6 8-11V5z"/></svg>Safety</div>
  <div class="value" style="left:53px;top:263px"><svg viewBox="0 0 24 24"><circle cx="12" cy="7" r="3.5"/><circle cx="5" cy="9" r="2.5"/><circle cx="19" cy="9" r="2.5"/><path d="M5 21v-3a7 7 0 0 1 14 0v3zM0 21v-2a5 5 0 0 1 4-4.8V21zM24 21v-2a5 5 0 0 0-4-4.8V21z"/></svg>Teamwork</div>
  <div class="value" style="left:270px;top:263px"><svg viewBox="0 0 24 24"><path d="M2 10h4v11H2zm6 11V10l5-8c1.5 0 2.5 1 2.2 2.6L14.5 9H21a2 2 0 0 1 2 2.3l-1.3 7.7A2.5 2.5 0 0 1 19.2 21z"/></svg>Trust</div>
</div>

<section class="services abs">
  <h2 class="section-title display abs" style="top:68px">Services</h2>
  <div class="service abs" style="left:102px;top:143px"><div class="service-icon" role="img" aria-label="Icon of a signed contract"></div><h3>General<br>Contracting</h3><p>Duis aute irure dolor in reilprehenderit in voluptate velit esse cillum do.</p><span class="link">READ MORE</span></div>
  <div class="service abs" style="left:358px;top:143px"><div class="service-icon" role="img" aria-label="Icon of a gear with a team"></div><h3>Construction<br>Management</h3><p>Duis aute irure dolor in reilprehenderit in voluptate velit esse cillum do.</p><span class="link">READ MORE</span></div>
  <div class="service abs" style="left:613px;top:143px"><div class="service-icon" role="img" aria-label="Icon of a crane beside a factory"></div><h3>Construction<br>Service</h3><p>Duis aute irure dolor in reilprehenderit in voluptate velit esse cillum do.</p><span class="link">READ MORE</span></div>
  <div class="service abs" style="left:856px;top:143px"><div class="service-icon" role="img" aria-label="Icon of a building blueprint"></div><h3>Design<br>Build</h3><p>Duis aute irure dolor in reilprehenderit in voluptate velit esse cillum do.</p><span class="link">READ MORE</span></div>
</section>

<h2 class="section-title display abs" style="top:2023px">Projects</h2>
<div class="project p1 abs" role="img" aria-label="Project photo: glass and metal office building"></div>
<div class="project p2 abs" role="img" aria-label="Project photo: blue industrial flex building with parking lot"></div>
<div class="project p3 abs" role="img" aria-label="Project photo: brick institutional building"></div>
<div class="project p4 abs" role="img" aria-label="Project photo: modern commercial building with glass storefront"></div>
<div class="view-more btn-outline abs">VIEW MORE</div>

<section class="testimonials abs">
  <h2 class="section-title display abs">Client Testimonials</h2>
  <div class="avatar abs" role="img" aria-label="Client portrait placeholder"></div>
  <p class="quote abs">“ Nemo enim ipsam voluptatem quia voluptas sit aslrn atur aut odit aut fugit, sed quia consequuntur magn do lores eos qui ratione voluptatem sequi nesciunt. Neque porro quisquam est, qui dolorem ipsum quia dolor sit amet, consectetur, adipisci velit, sed quia non numqam eius modi tempora incidunt ut lab.”</p>
  <div class="quote-author abs">- Marcus Ellery</div>
  <div class="quote-nav abs"><span><svg viewBox="0 0 9 9"><path d="M6 1 2.5 4.5 6 8"/></svg></span><span><svg viewBox="0 0 9 9"><path d="M3 1l3.5 3.5L3 8"/></svg></span></div>
</section>

<h2 class="section-title display abs" style="top:3626px">News</h2>
<article class="news-card abs" style="left:112px"><div class="news-photo n1" role="img" aria-label="News photo: site engineers in hard hats on a job site"></div><div class="news-body"><h3>Duis aute irure dolor in reprehen derit..</h3><div class="news-meta"><svg viewBox="0 0 24 24"><path d="M3 5h18v16H3zm2 5v9h14v-9zM7 2h2v4H7zm8 0h2v4h-2z"/></svg>30/04/2020 by Dana Whitcomb</div><p>Nemo enim ipsam voluptatm quia voluptas sit aspernaturi odit aut fugit, sed quia..</p><span class="link">READ MORE</span></div></article>
<article class="news-card abs" style="left:443px"><div class="news-photo n2" role="img" aria-label="News photo: construction site with crane at sunrise"></div><div class="news-body"><h3>Duis aute irure dolor in reprehen derit..</h3><div class="news-meta"><svg viewBox="0 0 24 24"><path d="M3 5h18v16H3zm2 5v9h14v-9zM7 2h2v4H7zm8 0h2v4h-2z"/></svg>30/04/2020 by Dana Whitcomb</div><p>Nemo enim ipsam voluptatm quia voluptas sit aspernaturi odit aut fugit, sed quia..</p><span class="link">READ MORE</span></div></article>
<article class="news-card abs" style="left:775px"><div class="news-photo n3" role="img" aria-label="News photo: construction crew members talking on site"></div><div class="news-body"><h3>Duis aute irure dolor in reprehen derit..</h3><div class="news-meta"><svg viewBox="0 0 24 24"><path d="M3 5h18v16H3zm2 5v9h14v-9zM7 2h2v4H7zm8 0h2v4h-2z"/></svg>30/04/2020 by Dana Whitcomb</div><p>Nemo enim ipsam voluptatm quia voluptas sit aspernaturi odit aut fugit, sed quia..</p><span class="link">READ MORE</span></div></article>

<footer class="site-footer abs">
  <div class="footer-divider abs" style="left:73px"></div>
  <div class="footer-divider abs" style="left:504px"></div>
  <div class="footer-brand abs">Halvern Ridge Construction</div>
  <div class="footer-col abs" style="left:583px;top:48px"><h4>Quick Links</h4><ul><li>About</li><li>Services</li><li>Projects</li><li>News</li><li>Contact</li></ul></div>
  <div class="footer-col abs" style="left:812px;top:48px"><h4>Contact Information</h4>
    <div class="footer-contact"><svg viewBox="0 0 24 24"><path d="M12 2a7 7 0 0 0-7 7c0 5 7 13 7 13s7-8 7-13a7 7 0 0 0-7-7zm0 9.5A2.5 2.5 0 1 1 12 6.5a2.5 2.5 0 0 1 0 5z"/></svg>4820 W Quarry Road<br><span style="padding-left:22px">Lindell, Utah 84190</span></div>
    <div class="footer-contact" style="margin-top:40px"><svg viewBox="0 0 24 24"><path d="M6.6 10.8a15.1 15.1 0 0 0 6.6 6.6l2.2-2.2a1 1 0 0 1 1-.25 11.4 11.4 0 0 0 3.6.57 1 1 0 0 1 1 1V20a1 1 0 0 1-1 1A17 17 0 0 1 3 4a1 1 0 0 1 1-1h3.5a1 1 0 0 1 1 1c0 1.25.2 2.45.57 3.57a1 1 0 0 1-.25 1z"/></svg>1 800 555 0142</div>
    <div class="footer-contact" style="margin-top:36px"><svg viewBox="0 0 24 24"><path d="M2 5h20v14H2zm2 2v.5l8 5 8-5V7l-8 5z"/></svg>info@halvernridgeconstruction.com</div>
  </div>
  <div class="footer-rule abs"></div>
  <div class="copyright abs">© 2021, Halvern Ridge Construction. All Rights Reserved.</div>
  <div class="social abs" style="left:991px" aria-label="Social profile link"></div>
  <div class="social abs" style="left:1042px" aria-label="Social profile link"></div>
</footer>

</body>
</html>
```